Business cards and stationary design

We just completed the design of our new logo and we need to print new business cards and letterhead for our nonprofit. We are looking for a fresh new design that shows off our new logo. On letterhead, we must have a column on the right or left to include our Board of Directors (up to 45 names) (see attachment)

Industry/Entity Type

Non-Profit

Contact Information for Business Card

Standard business card with name, title, Company name, mailing address phone numbers, email address and website. Tagline on back "Bringing the homeless home"

Font styles to use
Sans Serif

Requirements
Must have
• include pertinent information above
• new logo
• fonts compatible with logo
• should use logo colors only
Nice to have
• tag lines

```html
<!DOCTYPE html>
<html lang="en">
<head>
<meta charset="utf-8">
<title>Harbor Home Alliance – Business Card</title>
<link rel="stylesheet" href="https://fonts.googleapis.com/css2?family=Roboto:wght@400;500;700&display=swap">
<style>
  :root {
    --teal: #1688a8;
    --teal-deep: #0f7796;
    --sun: #f9b928;
    --red: #d9232d;
    --paper: #ffffff;
    --stage: #e6e7e9;
    --ink-light: #ffffff;
  }
  * { box-sizing: border-box; margin: 0; padding: 0; }
  html, body {
    width: 1200px; height: 911px; overflow: hidden;
    background: var(--stage);
    font-family: "Roboto", Arial, sans-serif;
  }
  .canvas { position: relative; width: 1200px; height: 911px; }

  .card {
    position: absolute;
    background: var(--paper);
    box-shadow: 0 10px 28px rgba(0,0,0,0.18);
    overflow: hidden;
  }

  /* Front card (portrait) */
  .card-front { left: 130px; top: 170px; width: 330px; height: 578px; }
  .front-artwork {
    position: absolute; left: 24px; top: 40px; width: 282px; height: 250px;
    background: linear-gradient(135deg, var(--teal) 0%, var(--teal) 45%, var(--sun) 46%, var(--sun) 100%);
  }
  .front-band { position: absolute; left: 0; top: 250px; width: 330px; height: 328px; }
  .front-details {
    position: absolute; left: 0; right: 0; top: 345px;
    text-align: center; color: var(--ink-light);
  }
  .person-name { font-size: 22px; font-weight: 700; letter-spacing: 0.5px; }
  .person-title { font-size: 14px; font-weight: 500; margin-top: 4px; letter-spacing: 0.5px; }
  .org-address { font-size: 13.5px; line-height: 1.35; margin-top: 14px; }
  .contact-lines { font-size: 13.5px; line-height: 1.35; margin-top: 12px; }

  /* Back card (landscape) */
  .card-back {
    left: 540px; top: 300px; width: 560px; height: 320px;
    display: flex; align-items: center; justify-content: center; gap: 14px;
  }
  .brand-dot { width: 22px; height: 22px; border-radius: 50%; background: var(--sun); }
  .brand-name {
    font-size: 30px; font-weight: 500; color: var(--teal);
    letter-spacing: 2px; text-transform: uppercase;
  }
</style>
</head>
<body>
<div class="canvas">

  <section class="card card-front">
    <div class="front-artwork" role="img" aria-label="Organisation emblem artwork: a house with a sunburst roof over teal buildings"></div>
    <svg class="front-band" viewBox="0 0 330 328" aria-hidden="true">
      <path d="M0 30 Q165 -20 330 150 L330 328 L0 328 Z" fill="var(--red)"/>
      <path d="M0 40 Q165 -5 330 170 L330 328 L0 328 Z" fill="var(--teal)"/>
    </svg>
    <div class="front-details">
      <p class="person-name">DANIEL REYES</p>
      <p class="person-title">CEO/FOUNDER</p>
      <p class="org-address">Harbor Home Alliance<br>1420 Cedar Ridge Road<br>Fairview, Oregon 97024</p>
      <p class="contact-lines">P. 555 210 4871<br>daniel@harborhome.org<br>www.harborhome.org</p>
    </div>
  </section>

  <section class="card card-back">
    <span class="brand-dot" aria-hidden="true"></span>
    <p class="brand-name">Harbor Home Alliance</p>
  </section>

</div>
</body>
</html>
```